Solvane Vitality MediSpa Brochure

We need a new brochure design. The old is attached.

We are wanting a three panel brochure for med spa designed and ready for print. The brochure will have content and images on both sides. We attached the old brochure in pdf format. The content needs to stay as on the attached pdf but please feel free to offer new designs. The color needs to match the attached logo, which is a light blue and teal. All images we want on the brochure are also attached.

The design must have an 1/8 in space from each edge for printing purposes

Target Market(s)

Men and Women

Industry/Entity Type

Wellness

Font styles to use
Sans Serif

Colors
34a6d7
33b8a4

Requirements
Must have
• soft curves. must have a 1/8 in space on all edges (including interior) to give bleed space for printing. Use content written on attached brochure.

```html
<!DOCTYPE html>
<html lang="en">
<head>
<meta charset="utf-8">
<title>Solvane Vitality MediSpa – Trifold Brochure</title>
<link href="https://fonts.googleapis.com/css2?family=Lato:wght@300;400;700&family=Oswald:wght@500&display=swap" rel="stylesheet">
<style>
  :root {
    --teal: #1fa0a5;
    --teal-deep: #0b5f68;
    --teal-pale: #e3f3f4;
    --ink: #222a2c;
    --heading: #0d5c66;
    --white: #ffffff;
    --page: #e6eaea;
  }
  * { margin: 0; padding: 0; box-sizing: border-box; }
  html, body { width: 1200px; height: 922px; overflow: hidden; }
  body { background: var(--page); font-family: "Lato", sans-serif; color: var(--ink); }

  .brochure { position: absolute; left: 40px; top: 30px; width: 1120px; height: 862px; background: var(--teal); box-shadow: 0 6px 20px rgba(0,0,0,.25); overflow: hidden; }
  .brochure__shapes { position: absolute; inset: 0; }
  .block { position: absolute; }

  .heading { font-size: 22px; line-height: 1.22; font-weight: 300; color: var(--heading); text-transform: uppercase; }
  .heading strong { font-weight: 700; display: block; }
  .copy { font-size: 13.5px; line-height: 19px; }
  .copy + .copy { margin-top: 6px; }
  .right { text-align: right; }

  .intro { left: 40px; top: 29px; width: 300px; }
  .intro .heading { margin-bottom: 14px; }
  .why { left: 40px; top: 226px; width: 300px; }
  .why .heading { margin-bottom: 10px; }

  .memberships { left: 37px; top: 533px; width: 270px; color: var(--white); }
  .memberships .heading { color: var(--white); margin-bottom: 16px; }
  .memberships .copy { color: var(--white); }
  .ticks { list-style: none; margin-top: 14px; font-weight: 700; font-size: 14px; line-height: 23.5px; }
  .ticks li::before { content: "✓"; margin-right: 8px; font-weight: 400; }

  .contact-line { display: flex; align-items: center; gap: 8px; color: var(--white); }
  .contact-line svg { flex: none; }
  .memberships__contact { left: 37px; top: 797px; }
  .phone-lg { font-size: 17px; letter-spacing: .5px; }
  .web { font-size: 14.5px; margin-top: 7px; }

  .doctor { left: 403px; top: 29px; width: 250px; }
  .doctor .heading strong { font-size: 22px; }
  .doctor .heading span { font-size: 19px; }
  .quotes { left: 403px; top: 99px; width: 245px; }
  .quotes .copy { margin: 0 0 17px; }

  .pin { left: 539px; top: 541px; width: 40px; height: 40px; }
  .visit { left: 397px; top: 596px; width: 325px; color: var(--white); text-align: center; }
  .address { font-size: 17px; line-height: 22px; letter-spacing: .3px; }
  .cta { display: inline-block; margin-top: 17px; width: 290px; height: 40px; line-height: 40px; border-radius: 20px; background: linear-gradient(#0f7a84, #0a5a62); font-family: "Oswald", sans-serif; font-size: 20px; letter-spacing: .5px; color: var(--white); box-shadow: 0 3px 6px rgba(0,0,0,.3); text-transform: uppercase; }
  .visit .contact-line { justify-content: center; margin-top: 8px; }
  .phone-bold { font-weight: 700; font-size: 18px; letter-spacing: .6px; }
  .email { font-size: 15px; }

  .brand { left: 760px; top: 70px; width: 360px; display: flex; align-items: center; justify-content: center; gap: 10px; }
  .brand__name { font-size: 25px; font-weight: 400; color: var(--teal); letter-spacing: .4px; white-space: nowrap; }
  .brand__mark { width: 18px; height: 18px; border-radius: 50%; background: var(--teal); flex: none; }

  .services { left: 775px; top: 580px; width: 230px; color: var(--white); }
  .services .heading { color: var(--white); font-size: 32px; line-height: 1.02; }
  .services .heading strong { font-size: 23px; }
  .services .ticks { font-weight: 300; font-size: 14.5px; line-height: 20.2px; margin-top: 8px; }
  .audience { left: 975px; top: 712px; width: 130px; text-align: right; font-weight: 700; font-size: 22px; line-height: 24px; color: var(--teal-deep); text-transform: uppercase; }
  .panel3__contact { left: 775px; top: 800px; }
</style>
</head>
<body>
<main class="brochure">
  <svg class="brochure__shapes" viewBox="0 0 1120 862" width="1120" height="862" aria-hidden="true">
    <path d="M372 677 C340 560 60 470 28 300 C10 150 70 40 130 0 L372 0 Z" fill="#ffffff"/>
    <path d="M372 677 C420 560 660 480 700 300 C720 180 690 60 640 0 L372 0 Z" fill="#f6f7f7"/>
    <path d="M372 677 C340 560 60 470 28 300 C10 150 70 40 130 0" fill="none" stroke="#0b5f68" stroke-width="9"/>
    <path d="M372 677 C420 560 660 480 700 300 C720 180 690 60 640 0" fill="none" stroke="#0b5f68" stroke-width="9"/>
    <line x1="372" y1="0" x2="372" y2="862" stroke="#0b5f68" stroke-opacity=".25"/>
    <rect x="747" y="0" width="373" height="862" fill="#ffffff"/>
    <path d="M747 0 L772 0 C782 60 800 110 835 140 L747 240 Z" fill="#1fa0a5"/>
    <path d="M747 545 L990 545 C1050 530 1095 480 1120 420 L1120 862 L747 862 Z" fill="#1fa0a5"/>
    <rect x="747" y="787" width="373" height="75" fill="#0b5f68"/>
    <circle cx="888" cy="328" r="221" fill="#ffffff"/>
    <circle cx="888" cy="328" r="212" fill="none" stroke="#0b5f68" stroke-width="7"/>
    <circle cx="888" cy="328" r="197" fill="none" stroke="#1fa0a5" stroke-width="10"/>
    <circle cx="647" cy="164" r="98" fill="#0b5f68"/>
    <circle cx="647" cy="164" r="92" fill="#1fa0a5"/>
    <circle cx="647" cy="164" r="86" fill="#ffffff"/>
  </svg>

  <svg class="block" style="left:970px;top:560px" width="150" height="240" viewBox="0 0 150 240" role="img" aria-label="Faint line illustration of a face beside the audience note"><path d="M150 0 C90 60 40 130 20 227 L150 240 Z" fill="#e3f3f4"/></svg>

  <div class="block" role="img" aria-label="Portrait photo of a woman with fresh glowing skin" style="left:705px;top:145px;width:366px;height:366px;border-radius:50%;background:radial-gradient(circle at 55% 45%, #f6dccd, #e9bfa9 60%, #c9a48e);"></div>
  <div class="block" role="img" aria-label="Portrait photo of the medical director outdoors" style="left:567px;top:84px;width:160px;height:160px;border-radius:50%;background:radial-gradient(circle at 50% 40%, #d9b59c, #6f8a5c 65%, #3f5a3a);"></div>

  <section class="block intro right">
    <h2 class="heading">Brookfield's <strong>Premier MediSpa</strong></h2>
    <p class="copy">Solvane Vitality MediSpa is the<br>premier medical spa in Brookfield, TX.<br>We utilize the best equipment available today<br>for laser treatments, dermal fillers, facials,<br>injections, chemical peels and<br>wellness solutions.</p>
  </section>

  <section class="block why right">
    <h2 class="heading">Why choose our <strong>MediSpa?</strong></h2>
    <p class="copy">Under the supervision of Dr. Elena Brandt,<br>our medical staff provides state-of-the-<br>art cosmetic treatments to both<br>women and men.</p>
    <p class="copy">Our staff is trained to provide unique<br>medicalspa services to help our<br>clients achieve a more<br>youthful look and defy<br>the aging process.</p>
  </section>

  <section class="block memberships">
    <h2 class="heading">Exclusive <strong>Memberships</strong></h2>
    <p class="copy">Our exclusive membership packages<br>are tailored for our clients and created<br>to give them an exceptional experience<br>at a discounted price.</p>
    <ul class="ticks">
      <li>SILVER Membership</li>
      <li>GOLD Membership</li>
      <li>PLATINUM Membership</li>
    </ul>
  </section>
  <div class="block memberships__contact">
    <p class="contact-line phone-lg"><svg width="16" height="16" viewBox="0 0 16 16"><circle cx="8" cy="8" r="7" fill="none" stroke="#fff" stroke-width="1.3"/><path d="M5.5 4.5l1.5 1.5-1 1c.5 1.2 1.4 2.1 2.6 2.6l1-1 1.5 1.5-1 1c-2.8-.4-5-2.6-5.4-5.4z" fill="#fff"/></svg>(555) 410-2275</p>
    <p class="contact-line web"><svg width="13" height="13" viewBox="0 0 14 14"><circle cx="7" cy="7" r="6" fill="none" stroke="#fff"/><ellipse cx="7" cy="7" rx="2.6" ry="6" fill="none" stroke="#fff"/><line x1="1" y1="7" x2="13" y2="7" stroke="#fff"/></svg>www.SolvaneVitalityMedispa.com</p>
  </div>

  <section class="block doctor">
    <h2 class="heading"><strong>Dr. Elena Brandt</strong><span>MD FACS</span></h2>
  </section>
  <section class="block quotes">
    <p class="copy">"Rejuvenation and<br>reconstruction of the<br>face are my passion,<br>whether it is to<br>improve one's visual<br>functions or to<br>enhance one's<br>appearance."</p>
    <p class="copy">"I personally perform all of<br>my injections and C02laser treatments<br>because safety and satisfaction are<br>my top priorities."</p>
    <p class="copy">"I was called by God to become a<br>physician at the age of seven<br>years old. I am motivated by<br>a desire to serve others by<br>providing superb<br>medical care.<br>I constantly<br>strive to do<br>my best."</p>
  </section>

  <svg class="block pin" viewBox="0 0 40 40" aria-hidden="true"><circle cx="20" cy="20" r="19" fill="#fff"/><path d="M20 10 a6.5 6.5 0 0 1 6.5 6.5 c0 5 -6.5 11.5 -6.5 11.5 s-6.5 -6.5 -6.5 -11.5 a6.5 6.5 0 0 1 6.5 -6.5z" fill="none" stroke="#1fa0a5" stroke-width="2"/><circle cx="20" cy="16.5" r="2.2" fill="#1fa0a5"/></svg>

  <section class="block visit">
    <p class="address">418 E. Harlow Ave<br>Suite 210<br>Brookfield TX 75099</p>
    <p class="cta">Schedule a Consultation</p>
    <p class="contact-line phone-bold"><svg width="17" height="17" viewBox="0 0 16 16"><circle cx="8" cy="8" r="7" fill="none" stroke="#fff" stroke-width="1.3"/><path d="M5.5 4.5l1.5 1.5-1 1c.5 1.2 1.4 2.1 2.6 2.6l1-1 1.5 1.5-1 1c-2.8-.4-5-2.6-5.4-5.4z" fill="#fff"/></svg>(555) 410-2281</p>
    <p class="contact-line phone-bold"><svg width="17" height="16" viewBox="0 0 17 16"><rect x="4" y="1" width="9" height="4" fill="#fff"/><rect x="1" y="5" width="15" height="7" rx="1.5" fill="#fff"/><rect x="4" y="10" width="9" height="5" fill="#fff" stroke="#1fa0a5"/></svg>(555) 410-2290</p>
    <p class="contact-line email" style="margin-top:11px"><svg width="14" height="10" viewBox="0 0 14 10"><rect x=".5" y=".5" width="13" height="9" fill="none" stroke="#fff"/><path d="M.5 .5l6.5 5 6.5-5" fill="none" stroke="#fff"/></svg>hello@elenabrandtmd.com</p>
    <p class="contact-line web"><svg width="13" height="13" viewBox="0 0 14 14"><circle cx="7" cy="7" r="6" fill="none" stroke="#fff"/><ellipse cx="7" cy="7" rx="2.6" ry="6" fill="none" stroke="#fff"/><line x1="1" y1="7" x2="13" y2="7" stroke="#fff"/></svg>www.SolvaneVitalityMedispa.com</p>
  </section>

  <header class="block brand">
    <span class="brand__mark"></span>
    <span class="brand__name">Solvane Vitality MediSpa</span>
  </header>

  <section class="block services">
    <h2 class="heading">Refresh <strong>and Rejuvenate</strong></h2>
    <ul class="ticks">
      <li>Laser Treatments</li>
      <li>Dermal Fillers</li>
      <li>Neurotoxins</li>
      <li>Facials</li>
      <li>Chemical Peels</li>
      <li>Wellness Treatments</li>
    </ul>
  </section>
  <p class="block audience">For<br>Women<br>&amp; Men</p>
  <div class="block panel3__contact">
    <p class="contact-line phone-lg"><svg width="16" height="16" viewBox="0 0 16 16"><circle cx="8" cy="8" r="7" fill="none" stroke="#fff" stroke-width="1.3"/><path d="M5.5 4.5l1.5 1.5-1 1c.5 1.2 1.4 2.1 2.6 2.6l1-1 1.5 1.5-1 1c-2.8-.4-5-2.6-5.4-5.4z" fill="#fff"/></svg>(555) 410-2275</p>
    <p class="contact-line web" style="font-size:15.5px"><svg width="13" height="13" viewBox="0 0 14 14"><circle cx="7" cy="7" r="6" fill="none" stroke="#fff"/><ellipse cx="7" cy="7" rx="2.6" ry="6" fill="none" stroke="#fff"/><line x1="1" y1="7" x2="13" y2="7" stroke="#fff"/></svg>www.SolvaneVitalityMedispa.com</p>
  </div>
</main>
</body>
</html>
```